Website redesign - vornatic.com

We are looking to do a full redesign of vornatic.com. Need a designer to come up overall layout and 3 specific pages and 3 different hero images.
Wireframes for the 3 pages are attached as well as site images. You don't have to follow the wireframes exactly, but instead the wireframe is there to show you the information that needs to be on each page. Feel free to rearrange as needed.
Our target market is self taught engineers. So definitely I want a more casual feel to it. I'm ok with fun bold colors as well. Really like websites that have the infinite scroll look/feel to them.
Looking to find a designer who will produce HTML and potentially even implement the HTML into our site checked in code.
HTML Code should be responsive/mobile first leveraging Bootstrap 4.
Attached files include:
0) Wireframe PDF
https://files.plexarbox.net/file/d/48K-7bQwTn3peRkW21xLmsZfYdgaCb/view?usp=sharing
1) Vornatic Images zip 1
https://files.plexarbox.net/file/d/48m5KZqT29Wr7sHyPbnDuwXcgEjsLF/view?usp=sharing
2) Vornatic Images zip 2
https://files.plexarbox.net/file/d/48uvd3MfTQ2nXbKpJaYeHsCwzLdGHN/view?usp=sharing
Target Market(s)
I sell DIY Waterproof Electronics enclosures. Target audience is self taught DIY engineers
Coding
Coded - Design and coding required
Number of Pages Required
3 page
Colors
Designer to choose colors to be used in the design.
Look and feel
Each slider illustrates characteristics of the customer's brand and the style your logo design should communicate.

```html
<!DOCTYPE html>
<html lang="en">
<head>
<meta charset="utf-8">
<title>Vornatic – Waterproof Project Boxes</title>
<link rel="stylesheet" href="https://fonts.googleapis.com/css2?family=Mulish:wght@400;600;700;800&family=Poppins:wght@700&display=swap">
<style>
:root{
  --blue:#0a0ae8;
  --lime:#c9d400;
  --ink:#2b2b2b;
  --muted:#666;
  --band:#f7f7f7;
  --dark:#232323;
  --white:#fff;
}
*{box-sizing:border-box;margin:0;padding:0}
html,body{width:1200px;height:4045px;overflow:hidden}
body{position:relative;font-family:"Mulish",sans-serif;color:var(--ink);background:var(--white)}
.abs{position:absolute}
.center{left:0;width:1200px;text-align:center}
.eyebrow{font-size:14px;letter-spacing:2px;color:var(--blue);font-weight:600;text-transform:uppercase}
.title{font-size:25px;font-weight:700;color:var(--ink);line-height:32px}
.btn{display:flex;align-items:center;justify-content:center;border-radius:20px;font-size:14px;font-weight:700;text-decoration:none}
.btn-outline{border:2px solid var(--blue);color:var(--ink);background:var(--white)}
.btn-blue{background:var(--blue);color:var(--white)}
.btn-lime{background:var(--lime);color:var(--white)}
.photo{position:absolute}

/* header */
.header{top:0;left:0;width:1200px;height:82px;background:var(--white)}
.brand{left:134px;top:18px;font-size:34px;font-weight:800;color:var(--blue);letter-spacing:-0.5px}
.nav a{position:absolute;top:32px;font-size:14px;color:var(--muted);text-decoration:none}
.signin{left:869px;top:22px;width:92px;height:31px;border:2px solid var(--lime);color:var(--ink);font-size:13px}
.signup{left:972px;top:22px;width:93px;height:31px;font-size:13px}

/* hero */
.hero{top:82px;left:0;width:1200px;height:507px;background:linear-gradient(135deg,#5a5e55,#3c3f3a 55%,#55584f)}
.hero-title{top:152px;font-family:"Poppins",sans-serif;font-size:39px;line-height:46px;color:var(--white)}
.hero-sub{top:270px;font-size:16px;letter-spacing:2.5px;font-weight:700;color:var(--white)}
.hero-btn{left:531px;top:314px;width:138px;height:38px}
.counter{left:134px;top:395px;font-size:24px;color:#ddd;font-weight:400}
.counter b{color:var(--lime);font-weight:400}

.band{left:0;width:1200px;background:var(--band)}

/* video */
.video{left:292px;top:842px;width:616px;height:360px;background:linear-gradient(160deg,#8a8f8c,#3d4241 60%,#6b6f6b)}
.video-bar{left:292px;top:1153px;width:616px;height:49px;background:#222}
.progress{left:382px;top:1176px;width:428px;height:2px;background:#555}
.progress span{position:absolute;left:0;top:-1px;width:75px;height:3px;background:var(--lime)}

/* carousel */
.card-shadow{box-shadow:0 4px 18px rgba(0,0,0,.08);background:var(--white)}
.arrow{width:40px;height:40px;border-radius:50%;display:flex;align-items:center;justify-content:center}

/* feature */
.feature-bg{left:586px;top:1866px;width:614px;height:461px;background:#f5f5f5}
.checks{left:652px;top:2048px;list-style:none;font-size:14px;color:#444;line-height:20px}
.checks li{position:relative;padding-left:31px;margin-bottom:14px;width:420px}
.checks svg{position:absolute;left:0;top:1px}

/* testimonials */
.quote-card{top:2501px;width:435px;height:220px}
.quote-text{font-size:14px;line-height:24px;color:#555;width:340px}
.quote-name{font-size:15px;color:var(--blue);font-weight:600;letter-spacing:.5px}
.quote-name::before{content:"";display:inline-block;width:18px;height:2px;background:var(--lime);vertical-align:middle;margin-right:16px}

/* examples */
.ex-card{width:294px;height:314px;background:var(--white)}
.ex-img{left:30px;top:30px;width:234px;height:176px;border-radius:4px}
.ex-cap{left:14px;top:223px;width:266px;height:91px;background:#f6f6f6;display:flex;align-items:center;justify-content:center;text-align:center;font-size:14px;line-height:22px;color:#333}
.ex-cap.active{background:var(--blue);color:var(--white);font-weight:600}

/* footer */
.footer{left:0;top:3711px;width:1200px;height:334px;background:var(--dark)}
.foot-brand{top:85px;font-size:40px;font-weight:600;color:#eee}
.foot-links{top:148px;font-size:12px;letter-spacing:1.5px;color:#bbb}
.foot-links span{margin:0 14px}
.social{top:187px;width:28px;height:28px;border:2px solid #ccc;border-radius:50%}
.copy{top:240px;font-size:13px;color:#bbb}
</style>
</head>
<body>

<header class="abs header">
  <div class="abs brand">Vornatic</div>
  <nav class="nav">
    <a style="left:338px" href="#">Get Started</a>
    <a style="left:441px" href="#">Designs</a>
    <a style="left:522px" href="#">FAQs</a>
    <a style="left:586px" href="#">Videos</a>
    <a style="left:660px" href="#">Contact Us</a>
  </nav>
  <a class="abs btn signin" href="#">Sign In</a>
  <a class="abs btn btn-blue signup" href="#">Sign Up</a>
</header>

<section class="abs hero" role="img" aria-label="Clear acrylic project box with stacked green circuit boards and terminal blocks">
</section>
<h1 class="abs center hero-title">Waterproof Project Boxes<br>Customized to Your Exact Needs.</h1>
<p class="abs center hero-sub">AT A FRACTION OF THE PRICE</p>
<a class="abs btn btn-lime hero-btn" href="#">Get Started</a>
<div class="abs counter"><b>01</b> /03</div>

<div class="abs band" style="top:905px;height:792px"></div>

<p class="abs center eyebrow" style="top:670px">Customize your</p>
<h2 class="abs center title" style="top:696px">Project Box Using Our Designer</h2>
<a class="abs btn btn-outline" style="left:531px;top:757px;width:138px;height:38px" href="#">Get Started</a>

<div class="abs video" role="img" aria-label="Video still of an assembled acrylic mounting kit with circuit boards and power supply"></div>
<div class="abs video-bar"></div>
<svg class="abs" style="left:320px;top:1168px" width="16" height="18" viewBox="0 0 16 18"><path d="M2 1l13 8-13 8z" fill="#fff"/></svg>
<div class="abs progress"><span></span></div>
<svg class="abs" style="left:868px;top:1168px" width="20" height="20" viewBox="0 0 20 20" fill="none" stroke="#ccc" stroke-width="1.6"><path d="M1 6V1h5M14 1h5v5M19 14v5h-5M6 19H1v-5M1 1l6 6M19 1l-6 6M19 19l-6-6M1 19l6-6"/></svg>

<p class="abs center eyebrow" style="top:1287px">Mounting kits for all the</p>
<h2 class="abs center title" style="top:1311px;font-size:24px">Popular Waterproof Project Boxes With Many Sizes to<br>Choose From</h2>
<a class="abs btn btn-outline" style="left:531px;top:1405px;width:138px;height:38px" href="#">Get Started</a>

<div class="abs card-shadow" style="left:135px;top:1554px;width:112px;height:174px"><div class="photo" style="inset:30px 0 30px 10px;background:linear-gradient(135deg,#6d7a5e,#2f3a2d)" role="img" aria-label="Circuit board on mounting plate"></div></div>
<div class="abs" style="left:247px;top:1525px;width:127px;height:238px;background:linear-gradient(160deg,#b8914e,#8d6a35)" role="img" aria-label="Bagged mounting hardware kit on cardboard"></div>
<div class="abs card-shadow" style="left:952px;top:1554px;width:113px;height:174px"><div class="photo" style="inset:30px 10px 30px 0;background:linear-gradient(135deg,#444,#1d1d1d)" role="img" aria-label="Black acrylic plate with relay boards"></div></div>
<div class="abs card-shadow" style="left:826px;top:1525px;width:126px;height:238px"><div class="photo" style="inset:40px 20px 60px 0;background:linear-gradient(135deg,#8a9b7f,#394236)" role="img" aria-label="Controller board on acrylic plate"></div></div>
<div class="abs card-shadow" style="left:374px;top:1497px;width:452px;height:291px">
  <div class="photo" style="left:60px;top:50px;width:330px;height:195px;background:radial-gradient(ellipse at center,#c9c9c4,#e9e9e6 60%,#fff 72%)" role="img" aria-label="Open grey waterproof enclosure with power supply inside"></div>
</div>
<div class="abs arrow" style="left:44px;top:1619px;background:var(--lime)"><svg width="12" height="14" viewBox="0 0 12 14"><path d="M8 1L3 7l5 6" fill="none" stroke="#fff" stroke-width="1.6"/></svg></div>
<div class="abs arrow" style="left:1113px;top:1619px;background:var(--blue)"><svg width="12" height="14" viewBox="0 0 12 14"><path d="M4 1l5 6-5 6" fill="none" stroke="#fff" stroke-width="1.6"/></svg></div>

<div class="abs" style="left:0;top:1866px;width:586px;height:461px;background:linear-gradient(135deg,#8c6a45,#b08a5d 45%,#7a5a39)" role="img" aria-label="Mounting plate laid on wood with boards, power supply and hardware"></div>
<div class="abs feature-bg"></div>
<p class="abs eyebrow" style="left:652px;top:1930px">Vornatic waterproof</p>
<h2 class="abs title" style="left:652px;top:1952px;font-size:28px;line-height:32px">Project Boxes Were Built by<br>Makers for Makers</h2>
<ul class="abs checks">
  <li><svg width="18" height="18" viewBox="0 0 18 18"><circle cx="9" cy="9" r="8" fill="none" stroke="#ccc"/><path d="M5 9l3 3 5-6" fill="none" stroke="var(--lime)" stroke-width="1.6"/></svg>Design to your specifications</li>
  <li><svg width="18" height="18" viewBox="0 0 18 18"><circle cx="9" cy="9" r="8" fill="none" stroke="#ccc"/><path d="M5 9l3 3 5-6" fill="none" stroke="var(--lime)" stroke-width="1.6"/></svg>Maker components: Nordino, Bramble Pi, Steadyvolt Power</li>
  <li><svg width="18" height="18" viewBox="0 0 18 18"><circle cx="9" cy="9" r="8" fill="none" stroke="#ccc"/><path d="M5 9l3 3 5-6" fill="none" stroke="var(--lime)" stroke-width="1.6"/></svg>Detailed build instructions, videos, walkthroughs</li>
  <li><svg width="18" height="18" viewBox="0 0 18 18"><circle cx="9" cy="9" r="8" fill="none" stroke="#ccc"/><path d="M5 9l3 3 5-6" fill="none" stroke="var(--lime)" stroke-width="1.6"/></svg>DIY made to look professional</li>
</ul>
<a class="abs btn btn-blue" style="left:652px;top:2228px;width:140px;height:39px" href="#">Get Started</a>

<p class="abs center eyebrow" style="top:2398px">What our</p>
<h2 class="abs center title" style="top:2421px;font-size:28px">Customers Have to Say</h2>

<div class="abs quote-card card-shadow" style="left:134px">
  <svg class="abs" style="left:-18px;top:38px" width="40" height="30" viewBox="0 0 40 30"><path d="M2 30V14Q2 2 14 0v6Q8 8 8 14h8v16zM22 30V14q0-12 12-14v6q-6 2-6 8h8v16z" fill="var(--lime)"/></svg>
  <p class="abs quote-text" style="left:40px;top:48px">Great work at a reasonable cost. I can't recommend them enough. If you're doing custom boxes for light shows, this is where you go.</p>
  <p class="abs quote-name" style="left:40px;top:150px">MARCUS D.</p>
</div>
<div class="abs quote-card card-shadow" style="left:630px">
  <svg class="abs" style="left:-18px;top:38px" width="40" height="30" viewBox="0 0 40 30"><path d="M2 30V14Q2 2 14 0v6Q8 8 8 14h8v16zM22 30V14q0-12 12-14v6q-6 2-6 8h8v16z" fill="var(--lime)"/></svg>
  <p class="abs quote-text" style="left:40px;top:48px">Fantastic service/product.. whether you simply generate the design and do all of the fabrication yourself or simply order the kits.</p>
  <p class="abs quote-name" style="left:40px;top:150px">TRENT H.</p>
</div>

<div class="abs band" style="top:2806px;height:905px"></div>
<p class="abs center eyebrow" style="top:2872px">See real</p>
<h2 class="abs center title" style="top:2892px;font-size:28px">Examples From Our Customers</h2>

<div class="abs ex-card" style="left:134px;top:2969px"><div class="abs ex-img" style="background:linear-gradient(135deg,#e8e8e8,#3a3a3a 55%,#e8e8e8)" role="img" aria-label="Black acrylic box with fan and controller board"></div><div class="abs ex-cap">KTR BRX8-72 w/Q16v3+<br>Extension Board</div></div>
<div class="abs ex-card" style="left:452px;top:2969px"><div class="abs ex-img" style="background:linear-gradient(160deg,#eee,#9a9a9a 45%,#222 70%,#eee)" role="img" aria-label="Stacked power supplies on black mounting plates"></div><div class="abs ex-cap active">KTR BRX8-72 w/Q16v3+<br>Extension Board</div></div>
<div class="abs ex-card" style="left:771px;top:2969px"><div class="abs ex-img" style="background:linear-gradient(160deg,#eee,#4d6a4a 40%,#222 65%,#eee)" role="img" aria-label="Two-level acrylic mount with green boards"></div><div class="abs ex-cap">KTR BRX8-72 w/Q16v3+<br>Extension Board</div></div>
<div class="abs ex-card" style="left:134px;top:3315px"><div class="abs ex-img" style="background:linear-gradient(160deg,#eee,#3f5a3c 40%,#222 65%,#eee)" role="img" aria-label="Layered board mount with spacers"></div><div class="abs ex-cap">KTR BRX8-72 w/Q16v3+<br>Extension Board</div></div>
<div class="abs ex-card" style="left:452px;top:3315px"><div class="abs ex-img" style="background:linear-gradient(135deg,#eee,#b48a52 40%,#c9a06a 65%,#eee)" role="img" aria-label="Unassembled cardboard-coloured panel kit with hardware"></div><div class="abs ex-cap">KTR BRX8-72 w/Q16v3+<br>Extension Board</div></div>
<div class="abs ex-card" style="left:771px;top:3315px"><div class="abs ex-img" style="background:linear-gradient(135deg,#eee,#777 35%,#2d3a2b 65%,#eee)" role="img" aria-label="Power supply and controller on black plate"></div><div class="abs ex-cap">KTR BRX8-72 w/Q16v3+<br>Extension Board</div></div>

<footer class="abs footer">
  <div class="abs center foot-brand">Vornatic</div>
  <p class="abs center foot-links">GET STARTED<span>|</span>DESIGNS<span>|</span>FAQS<span>|</span>VIDEOS<span>|</span>CONTACT US</p>
  <div class="abs social" style="left:565px"></div>
  <div class="abs social" style="left:605px"></div>
  <p class="abs center copy">Copyright 2020 Vornatic.</p>
</footer>

</body>
</html>
```